Menu Design Project for an Italian cafe

Casual Italian style cafe situated in Chinatown in Sydney Australia . Value for money food, good coffee and good location are the cafes strengths. Catering to bushiness crowd in the morning/lunch, tourist crowd for brunch and Asian customers for late afternoon coffee.
Design concept is understated, casual European chic. Should communicate a casual escape to have a good meet up with friends to escape the hustle and bustle of the city crowd.
Would like to move away from current colors of dark brown, creme, black and orange. Would like a more enticing vibrant and brighter colour scheme.

```html
<!DOCTYPE html>
<html lang="en">
<head>
<meta charset="utf-8">
<title>Piatto – Menu Set</title>
<link rel="stylesheet" href="https://fonts.googleapis.com/css2?family=Oswald:wght@300;400&family=Crimson+Text:wght@400;600&display=swap">
<style>
  :root {
    --backdrop: #e4e6e6;
    --paper: #fbfbf9;
    --paper-shade: #f1f1ee;
    --teal: #14938f;
    --teal-cover: #17a398;
    --teal-cover-deep: #0f8f86;
    --red: #e0202c;
    --red-cover: #c8393a;
    --red-cover-deep: #b52f31;
    --green-cover: #7fce55;
    --green-cover-deep: #6cc046;
    --spine: #0e4560;
    --cover-ink: #173f52;
    --body-ink: #222;
    --rivet: #cfd2d3;
  }
  * { box-sizing: border-box; margin: 0; padding: 0; }
  html, body { width: 1200px; height: 900px; overflow: hidden; }
  body { background: var(--backdrop); position: relative; font-family: "Crimson Text", Georgia, serif; }

  .menu-page {
    position: absolute; top: 22px; height: 613px;
    background: var(--paper); overflow: hidden;
    box-shadow: 0 2px 6px rgba(0,0,0,.18);
  }
  .menu-page--left { left: 270px; width: 436px; }
  .menu-page--right { left: 706px; width: 440px; background: linear-gradient(90deg, var(--paper-shade), var(--paper) 12%); }

  .page-rule { position: absolute; top: 44px; height: 6px; border-top: 2px solid var(--teal); border-bottom: 1px solid var(--teal); }
  .menu-page--left .page-rule { left: 44px; width: 352px; }
  .menu-page--right .page-rule { left: 42px; width: 352px; }

  .menu-column { position: absolute; top: 60px; width: 156px; }
  .menu-page--left .menu-column--a { left: 44px; }
  .menu-page--left .menu-column--b { left: 240px; }
  .menu-page--right .menu-column--a { left: 42px; }
  .menu-page--right .menu-column--b { left: 238px; }

  .section-title {
    font-family: "Oswald", sans-serif; font-weight: 400; font-size: 14px;
    text-align: center; text-transform: uppercase; color: var(--red); line-height: 20px;
  }
  .section-title--teal { color: var(--teal); }

  .dish { position: relative; margin-bottom: 17px; }
  .dish-name {
    font-family: "Oswald", sans-serif; font-weight: 400; font-size: 14px;
    text-transform: uppercase; color: var(--teal); line-height: 17px; letter-spacing: .2px;
  }
  .dish-name--red { color: var(--red); }
  .dish-name--plain { font-family: "Crimson Text", serif; font-weight: 600; text-transform: none; color: var(--body-ink); font-size: 12.5px; }
  .dish-text { font-size: 10px; line-height: 11px; color: var(--body-ink); }
  .dish-price { position: absolute; right: -22px; top: -2px; font-size: 8px; font-weight: 600; color: var(--body-ink); }

  .column-rule { border-top: 1px solid var(--teal); margin: -6px 0 10px; }
  .menu-note { font-size: 10px; line-height: 11px; text-align: center; color: var(--body-ink); margin-bottom: 8px; }

  .menu-cover {
    position: absolute; overflow: hidden;
    box-shadow: 2px 4px 10px rgba(0,0,0,.35);
  }
  .menu-cover::before {
    content: ""; position: absolute; left: 0; top: 0; bottom: 0; width: 41px; background: var(--spine);
  }
  .menu-cover--bill { left: 232px; top: 585px; width: 216px; height: 305px; background: linear-gradient(160deg, var(--green-cover), var(--green-cover-deep)); }
  .menu-cover--drinks { left: 471px; top: 280px; width: 239px; height: 610px; background: linear-gradient(160deg, var(--red-cover), var(--red-cover-deep)); }
  .menu-cover--food { left: 731px; top: 280px; width: 434px; height: 610px; background: linear-gradient(160deg, var(--teal-cover), var(--teal-cover-deep)); }

  .rivet {
    position: absolute; left: 8px; width: 25px; height: 25px; border-radius: 50%;
    background: radial-gradient(circle at 40% 35%, #f2f3f3, var(--rivet) 55%, #9a9fa1);
  }

  .cover-title {
    position: absolute; left: 41px; right: 0; text-align: center;
    font-family: "Oswald", sans-serif; font-weight: 300; font-size: 21px;
    letter-spacing: 3px; text-transform: uppercase; color: var(--cover-ink); line-height: 52.5px;
  }
  .cover-title span { text-decoration: underline; text-decoration-thickness: 1.5px; text-underline-offset: 5px; }

  .brand {
    position: absolute; left: 41px; right: 0; display: flex; justify-content: center; align-items: center; gap: 8px;
    font-family: "Oswald", sans-serif; font-weight: 400; color: var(--cover-ink);
  }
  .brand-dot { border: 2px solid var(--cover-ink); border-radius: 50%; }
</style>
</head>
<body>

<section class="menu-page menu-page--left">
  <div class="page-rule"></div>
  <div class="menu-column menu-column--a">
    <h2 class="section-title">Pasta</h2>
    <div class="dish"><span class="dish-price">14.99</span><h3 class="dish-name">Vongole Tagliolini</h3><p class="dish-text">The best Italian carpet shell clams cooked with chilli, garlic, parsley, white wine &amp; olive oil.</p></div>
    <div class="dish"><span class="dish-price">14.29</span><h3 class="dish-name">Spaghetti alla Norma</h3><p class="dish-text">A classic Sicilian pasta dish of ubergines, oregano, chilli &amp; basil, all in a rich tomato sauce.</p></div>
    <div class="dish"><span class="dish-price">14.29</span><h3 class="dish-name">Tagliatelle Bolognese</h3><p class="dish-text">Ragù of British beef &amp; pork, with herbs, Chianti, Parmesan &amp; crunchy, herby breadcrumbs.</p></div>
    <div class="dish"><span class="dish-price">14.29</span><h3 class="dish-name">Prawn Linguine</h3><p class="dish-text">Fried garlicky prawns, shaved fennel, tomatoes, chilli &amp; rocket.</p></div>
    <div class="dish"><h3 class="dish-name">Black Angel Spaghetti</h3><p class="dish-text">British scallops, garlic, chilli, anchovies, wine, parsley, capers &amp; squid ink pasta.</p></div>
    <div class="column-rule"></div>
    <h2 class="section-title">Special Pasta</h2>
    <div class="dish"><h3 class="dish-name">Vongole Tagliolini</h3><p class="dish-text">The best Italian carpet shell clams cooked with chilli, garlic, parsley, white wine &amp; olive oil.</p></div>
    <div class="dish"><h3 class="dish-name">Spaghetti alla Norma</h3><p class="dish-text">A classic Sicilian pasta dish of ubergines, oregano, chilli &amp; basil, all in a rich tomato sauce.</p></div>
    <div class="column-rule"></div>
    <p class="menu-note">All dishes are fresh and made on the spot. Remember to ask for wine.</p>
    <div class="column-rule" style="margin-top:0"></div>
  </div>
  <div class="menu-column menu-column--b">
    <h2 class="section-title section-title--teal">Hot and Spicy</h2>
    <div class="dish"><span class="dish-price">14.99</span><h3 class="dish-name dish-name--red">Vongole Tagliolini</h3><p class="dish-text">The best Italian carpet shell clams cooked with chilli, garlic, parsley, white wine &amp; olive oil.</p></div>
    <div class="dish"><span class="dish-price">14.29</span><h3 class="dish-name dish-name--red">Spaghetti alla Norma</h3><p class="dish-text">A classic Sicilian pasta dish of ubergines, oregano, chilli &amp; basil, all in a rich tomato sauce.</p></div>
    <div class="dish"><span class="dish-price">14.29</span><h3 class="dish-name dish-name--plain">Some Dish With Things</h3><p class="dish-text">Ragù of British beef &amp; pork, with herbs, Chianti, Parmesan &amp; crunchy, herby breadcrumbs.</p></div>
    <div class="column-rule"></div>
    <h2 class="section-title section-title--teal">Prawn Linguine</h2>
  </div>
</section>

<section class="menu-page menu-page--right">
  <div class="page-rule"></div>
  <div class="menu-column menu-column--a">
    <h2 class="section-title">Pasta</h2>
    <div class="dish"><span class="dish-price">14.99</span><h3 class="dish-name">Vongole Tagliolini</h3><p class="dish-text">The best Italian carpet shell clams cooked with chilli, garlic, parsley, white wine &amp; olive oil.</p></div>
    <div class="dish"><span class="dish-price">14.29</span><h3 class="dish-name">Spaghetti alla Norma</h3><p class="dish-text">A classic Sicilian pasta dish of ubergines, oregano, chilli &amp; basil, all in a rich tomato sauce.</p></div>
    <div class="dish"><span class="dish-price">14.29</span><h3 class="dish-name">Tagliatelle Bolognese</h3><p class="dish-text">Ragù of British beef &amp; pork, with herbs, Chianti, Parmesan &amp; crunchy, herby breadcrumbs.</p></div>
    <div class="dish"><h3 class="dish-name">Prawn Linguine</h3></div>
  </div>
  <div class="menu-column menu-column--b">
    <h2 class="section-title section-title--teal">Hot and Spicy</h2>
    <div class="dish"><span class="dish-price">14.99</span><h3 class="dish-name dish-name--red">Vongole Tagliolini</h3><p class="dish-text">The best Italian carpet shell clams cooked with chilli, garlic, parsley, white wine &amp; olive oil.</p></div>
    <div class="dish"><span class="dish-price">14.29</span><h3 class="dish-name dish-name--red">Spaghetti alla Norma</h3><p class="dish-text">A classic Sicilian pasta dish of ubergines, oregano, chilli &amp; basil, all in a rich tomato sauce.</p></div>
    <div class="dish"><span class="dish-price">14.29</span><h3 class="dish-name dish-name--plain">Some Dish With Things</h3><p class="dish-text">Ragù of British beef &amp; pork, with herbs, Chianti, Parmesan &amp; crunchy, herby breadcrumbs.</p></div>
    <div class="column-rule"></div>
    <h2 class="section-title section-title--teal">Prawn Linguine</h2>
  </div>
</section>

<section class="menu-cover menu-cover--drinks">
  <span class="rivet" style="top:132px"></span>
  <span class="rivet" style="top:443px"></span>
  <h2 class="cover-title" style="top:190px"><span>Wines and</span><br><span>Beers</span><br><span>and delicious</span><br><span>fresh</span><br><span>cocktails</span></h2>
  <div class="brand" style="top:512px;font-size:24px"><span class="brand-dot" style="width:26px;height:26px"></span>Piatto</div>
</section>

<section class="menu-cover menu-cover--food">
  <span class="rivet" style="top:135px"></span>
  <span class="rivet" style="top:443px"></span>
  <h2 class="cover-title" style="top:191px"><span>Pastas and</span><br><span>delicious crostinis</span><br><span>as fresh</span><br><span>as a Tuscan spring</span></h2>
  <div class="brand" style="top:512px;font-size:24px"><span class="brand-dot" style="width:26px;height:26px"></span>Piatto</div>
</section>

<section class="menu-cover menu-cover--bill">
  <span class="rivet" style="top:62px"></span>
  <span class="rivet" style="top:215px"></span>
  <h2 class="cover-title" style="top:86px"><span>Your</span><br><span>Bill</span></h2>
  <div class="brand" style="top:250px;font-size:20px"><span class="brand-dot" style="width:22px;height:22px"></span>Piatto</div>
</section>

</body>
</html>
```